Electrical Contractors Business Card Design

I need a business card design for an electrical contracting business. A theme I was thinking of is the BE of Brightway Electrical both facing each other ie the second E is back to front and maybe each horizontal part of the E's are a different colours of the internal wires of TPS cable. The top would be blue(representing the sky), the middle green(representing the grass) and the lower would be brown(representing below the earth) (neutral,earth and active). And coming out of the back of each E going to each side of the business card would be the white outer sheath of TPS cable. I would like a big part of the card to be a very bright emerald flourescent green and maybe silver for the top half. the message I would like to send is that of an environmentally friendly, ethical business that delivers quality sevice on time.

Target Market(s)

40 to 80 year old home owners

Industry/Entity Type

Electrical

Contact Information for Business Card

Tom Keller
Brightway Electrical
EC 274381
Mob: 0417 592 064

```html
<!DOCTYPE html>
<html lang="en">
<head>
<meta charset="utf-8">
<title>Brightway Electrical – Business Card</title>
<link rel="stylesheet" href="https://fonts.googleapis.com/css2?family=Open+Sans:wght@700;800&display=swap">
<style>
  :root {
    --green-bright: #1aa64a;
    --green-deep: #075e25;
    --green-ring: #4cb848;
    --green-text: #0b6b2b;
    --white: #ffffff;
  }
  html, body {
    margin: 0;
    padding: 0;
    width: 1200px;
    height: 695px;
    overflow: hidden;
    background: var(--white);
  }
  .card {
    position: relative;
    width: 1200px;
    height: 695px;
    overflow: hidden;
    font-family: "Open Sans", Arial, sans-serif;
    color: var(--white);
  }
  .card__backdrop {
    position: absolute;
    inset: 0;
  }
  .services {
    position: absolute;
    top: 36px;
    left: 0;
    width: 1200px;
    margin: 0;
    padding: 0;
    list-style: none;
    display: flex;
    justify-content: center;
    gap: 26px;
    font-weight: 800;
    font-size: 19px;
    letter-spacing: 0.2px;
  }
  .services__item::before {
    content: "";
    display: inline-block;
    width: 12px;
    height: 12px;
    margin-right: 16px;
    border-radius: 50%;
    background: var(--white);
    vertical-align: 2px;
  }
  .badge {
    position: absolute;
    left: 405px;
    top: 152px;
    width: 418px;
    height: 418px;
    display: flex;
    flex-direction: column;
    align-items: center;
    justify-content: center;
    text-align: center;
  }
  .badge__name {
    margin: 0;
    font-weight: 800;
    font-size: 38px;
    line-height: 1.12;
    color: var(--green-text);
    letter-spacing: 0.5px;
  }
  .badge__licence {
    margin: 18px 0 0;
    font-weight: 800;
    font-size: 24px;
    color: var(--green-text);
  }
  .mobile {
    position: absolute;
    left: 0;
    width: 1200px;
    top: 612px;
    margin: 0;
    text-align: center;
    font-weight: 800;
    font-size: 50px;
    line-height: 1;
    letter-spacing: 0.5px;
  }
</style>
</head>
<body>
  <main class="card">
    <svg class="card__backdrop" width="1200" height="695" viewBox="0 0 1200 695" aria-hidden="true">
      <rect class="band-top" width="1200" height="695" fill="var(--green-bright)"/>
      <path class="band-lower" d="M0,186 C230,172 330,230 410,330 L790,330 C870,230 970,172 1200,166 L1200,695 L0,695 Z" fill="var(--green-deep)"/>
      <path class="sheath-line" d="M0,180 C230,166 330,224 410,324 M790,324 C870,224 970,166 1200,160" fill="none" stroke="var(--white)" stroke-width="12"/>
      <circle class="badge-ring" cx="614" cy="361" r="240" fill="var(--green-ring)"/>
      <circle class="badge-face" cx="614" cy="361" r="208" fill="var(--white)"/>
    </svg>

    <ul class="services">
      <li class="services__item">ELECTRICAL WIRING &amp; CONSTRUCTION</li>
      <li class="services__item">COMMERCIAL LIGHTING</li>
      <li class="services__item">ADD CUSTOMER HIGHLIGHT</li>
    </ul>

    <div class="badge">
      <p class="badge__name">TOM KELLER<br>BRIGHTWAY<br>ELECTRICAL</p>
      <p class="badge__licence">LICENCE # EC274381</p>
    </div>

    <p class="mobile">MOBILE # 0417 592 064</p>
  </main>
</body>
</html>
```